Gospel Tract titled "A Clear Road Upward From Iowa."

This will be a bi-fold brochure. The design will be in the front panel of the brochure which is 4 inches wide and 8.5 inches high. This is a common brochure among Gospel tracts in the series, "A Clear Road Upward from ______________ ." The blank is usually a state, city, or other location. I want a "fun" image of Iowa or something representing Iowa at the bottom. A graphic representing "heaven" at the top. Perhaps a meandering road between the two. The words, "A Clear Road Upward from Iowa", but be on the front somewhere. I am also open to other designs with this theme and the words "A Clear Road Upward from Iowa." My suggestion is just one idea.

Target Market(s)

Non-Christians who are interested in knowing how to get to heaven

Requirements
Must have
• Something specific to the state of Iowa at the bottom: farms, state fair, cows, barns, power windmills, the capitol building, etc.
Nice to have
• I would like something bright, colorful, with a fun Iowa image at the bottom.
Should not have
• Religous symbolism....no doves, angels, crosses, etc.

```html
<!DOCTYPE html>
<html lang="en">
<head>
<meta charset="utf-8">
<title>A Clear Road Upward From Iowa</title>
<link rel="stylesheet" href="https://fonts.googleapis.com/css2?family=Anton&family=Bebas+Neue&family=Kaushan+Script&display=swap">
<style>
  :root {
    --sky-top: #4a78d8;
    --sky-mid: #8e8fe0;
    --cloud-pink: #d79ad6;
    --cloud-violet: #9a78d0;
    --sun-glow: #fff7d6;
    --horizon-orange: #ff7a1e;
    --horizon-red: #e2321c;
    --city-dusk: #3d4a66;
    --city-shadow: #1f2636;
    --city-light: #c9a878;
    --ink-navy: #0d1670;
    --ink-deep: #16195a;
    --ink-black: #111018;
    --iowa-top: #0c1a78;
    --iowa-mid: #3a1f7a;
    --iowa-low: #e8361a;
    --iowa-base: #ff6a14;
  }
  html, body {
    margin: 0;
    padding: 0;
    width: 1200px;
    height: 2550px;
    overflow: hidden;
    background: #ffffff;
  }
  .cover {
    position: relative;
    width: 1200px;
    height: 2550px;
    overflow: hidden;
  }
  .sky-art {
    position: absolute;
    left: 0; top: 0;
    width: 1200px;
    height: 1820px;
    background:
      radial-gradient(circle at 600px 690px, var(--sun-glow) 0, rgba(255,247,214,0.85) 60px, rgba(255,230,200,0.35) 200px, rgba(255,255,255,0) 420px),
      radial-gradient(ellipse 900px 260px at 600px 1740px, var(--horizon-orange) 0, var(--horizon-red) 45%, rgba(226,50,28,0) 100%),
      radial-gradient(ellipse 420px 260px at 180px 1150px, var(--cloud-pink) 0, rgba(215,154,214,0) 100%),
      radial-gradient(ellipse 420px 260px at 1040px 1100px, var(--cloud-pink) 0, rgba(215,154,214,0) 100%),
      radial-gradient(ellipse 500px 300px at 980px 420px, var(--cloud-violet) 0, rgba(154,120,208,0) 100%),
      radial-gradient(ellipse 500px 300px at 160px 440px, var(--cloud-violet) 0, rgba(154,120,208,0) 100%),
      linear-gradient(180deg, var(--sky-top) 0%, var(--sky-mid) 40%, var(--cloud-pink) 70%, var(--horizon-orange) 96%, var(--horizon-red) 100%);
  }
  .stairway {
    position: absolute;
    left: 0; top: 0;
  }
  .city-art {
    position: absolute;
    left: 0; top: 1810px;
    width: 1200px;
    height: 740px;
    background:
      radial-gradient(ellipse 260px 500px at 640px 560px, var(--city-light) 0, rgba(201,168,120,0) 100%),
      linear-gradient(180deg, #6c5a66 0%, var(--city-dusk) 18%, var(--city-shadow) 100%);
  }
  .title {
    position: absolute;
    left: 0; top: 0;
    width: 1200px;
    margin: 0;
    text-align: center;
    font-weight: 400;
  }
  .title span { position: absolute; left: 0; width: 1200px; display: block; }
  .title-line-1 {
    top: 288px;
    font-family: "Bebas Neue", "Oswald", sans-serif;
    font-size: 210px;
    line-height: 1;
    color: var(--ink-navy);
    letter-spacing: 2px;
  }
  .title-line-2 {
    top: 462px;
    font-family: "Bebas Neue", "Oswald", sans-serif;
    font-size: 200px;
    line-height: 1;
    color: var(--ink-navy);
    letter-spacing: 2px;
  }
  .title-script {
    top: 615px;
    font-family: "Kaushan Script", "Brush Script MT", cursive;
    font-size: 290px;
    line-height: 1.1;
    color: var(--ink-black);
    transform: rotate(-4deg);
  }
  .title-from {
    top: 1168px;
    font-family: "Bebas Neue", "Oswald", sans-serif;
    font-size: 272px;
    line-height: 1;
    color: var(--ink-deep);
    letter-spacing: 4px;
  }
  .title-place {
    top: 1376px;
    font-family: "Anton", "Impact", sans-serif;
    font-size: 495px;
    line-height: 1;
    letter-spacing: 6px;
    background: linear-gradient(180deg, var(--iowa-top) 0%, var(--iowa-top) 35%, var(--iowa-mid) 55%, var(--iowa-low) 80%, var(--iowa-base) 100%);
    -webkit-background-clip: text;
    background-clip: text;
    color: transparent;
  }
</style>
</head>
<body>
  <main class="cover">
    <div class="sky-art" role="img" aria-label="Painted sky of pink and violet clouds with a bright sun and a stairway rising toward it, fading into an orange sunset horizon"></div>
    <svg class="stairway" width="1200" height="1820" viewBox="0 0 1200 1820" aria-hidden="true">
      <defs>
        <linearGradient id="stair-fill" x1="0" y1="0" x2="0" y2="1">
          <stop offset="0" stop-color="#f4dcff" stop-opacity="0.2"/>
          <stop offset="1" stop-color="#b06ad8" stop-opacity="0.55"/>
        </linearGradient>
      </defs>
      <polygon points="580,900 620,900 760,1700 440,1700" fill="url(#stair-fill)"/>
    </svg>
    <div class="city-art" role="img" aria-label="Aerial evening view of a downtown Iowa street lined with lit buildings leading to a domed old capitol"></div>
    <h1 class="title">
      <span class="title-line-1">A Clear</span>
      <span class="title-line-2">Road</span>
      <span class="title-script">Upward</span>
      <span class="title-from">From</span>
      <span class="title-place">IOWA</span>
    </h1>
  </main>
</body>
</html>
```